New Website for novelty yarn producer

We need a new website for our company, Tarvek. We make highly tailored yarns for weavers worldwide. This year marks our 40th anniversary and we want to evolve our image and identity.

Our temporary website can be found at:
www.tarvekyarns.com

Our only concern in that throughout the website the protagonist must be our client, we make their creations possible and are highly adaptable both during the ideation process of the yarn as well as in the production. This is at the core of the way we do business and is summarised within the concept of FPM (Fluid Partner Method).

Industry/Entity Type

Textile

Number of Pages Required

1 page

Colors
9bcb3c

Requirements
Must have
• Fluid Partner Method (FPM) - can be found on or current website www.tarvekyarns.com

```html
<!DOCTYPE html>
<html lang="en">
<head>
<meta charset="utf-8">
<title>Tarvek Novelty Yarn Solutions</title>
<link href="https://fonts.googleapis.com/css2?family=Roboto:wght@300;400;500;700;900&display=swap" rel="stylesheet">
<style>
:root{
  --green:#9bcb3c;
  --green-soft:#bcdc8a;
  --green-bar:rgba(155,203,60,.88);
  --ink:#1d1d1b;
  --grey:#6b6b6b;
  --dark:#3a3a3a;
  --white:#ffffff;
}
*{margin:0;padding:0;box-sizing:border-box}
html,body{width:1200px;height:3854px;overflow:hidden}
body{font-family:'Roboto',sans-serif;background:var(--white);color:var(--ink);position:relative}
section,header,footer{position:absolute;left:0;width:1200px}

/* header */
.site-header{top:0;height:103px;background:var(--white)}
.brand{position:absolute;left:46px;top:22px;font-weight:700;font-size:40px;letter-spacing:1px;color:var(--ink);line-height:1}
.brand-sub{position:absolute;left:48px;top:66px;font-size:10px;letter-spacing:1.5px;color:var(--grey);text-transform:uppercase}
.main-nav{position:absolute;right:54px;top:44px;display:flex;gap:30px;font-size:17px;font-weight:500;text-transform:uppercase;white-space:nowrap}
.main-nav span.more::after{content:"\2304";color:var(--green);margin-left:3px}

/* hero */
.hero{top:103px;height:809px;background:linear-gradient(160deg,#4e8f8a 0%,#b9c7b8 20%,#e7e2d6 35%,#9bcb3c 55%,#c12c3b 72%,#e34d2a 85%,#f2a13a 100%)}
.hero-bar{position:absolute;height:108px;background:var(--green-bar);display:flex;align-items:center;font-weight:700;font-size:76px;letter-spacing:1px;white-space:nowrap}
.hero-bar.one{top:295px;left:0;width:750px;padding-left:205px;color:var(--ink)}
.hero-bar.two{top:424px;left:236px;width:535px;padding-left:200px;color:var(--white)}
.hero-bar.three{top:545px;left:378px;width:642px;padding-left:203px;color:var(--ink)}
.badge{position:absolute;left:576px;width:48px;height:48px;background:var(--green);transform:rotate(45deg);border:3px solid var(--white)}

/* values */
.values{top:960px;height:330px}
.value{position:absolute;top:50px;width:250px;text-align:center}
.value h3{font-size:29px;font-weight:700;text-transform:uppercase;color:var(--ink);white-space:nowrap}
.value h3::after{content:"";display:block;width:150px;height:3px;background:var(--green);margin:6px auto 16px}
.value p{font-size:14px;line-height:22px;color:var(--dark)}

/* offer */
.offer-band{top:1321px;height:62px;background:var(--green);text-align:center;font-size:29px;font-weight:700;line-height:62px;text-transform:uppercase}
.offer-tiles{top:1388px;height:406px;display:flex}
.tile{width:400px;height:406px;position:relative;text-align:center;color:var(--white)}
.tile.network{background:linear-gradient(135deg,#2a1f24,#5a2030 50%,#1a1a1a)}
.tile.fabric{background:linear-gradient(150deg,#4d5a2c,#9bcb3c 45%,#c9d3b0 70%,#6f7a63)}
.tile.production{background:linear-gradient(135deg,#5b1d25,#3a2a1e 50%,#6d5a1f)}
.tile svg{position:absolute;left:160px;top:60px}
.tile h4{position:absolute;top:202px;width:100%;font-size:18px;font-weight:700;color:var(--green);text-transform:uppercase}
.tile p{position:absolute;top:245px;left:60px;width:280px;font-size:13px;line-height:20px}

/* method */
.method{top:1794px;height:468px;background:linear-gradient(165deg,#3d6f7a 0%,#c8c3b5 25%,#9bcb3c 45%,#b8283a 65%,#e2502b 80%,#f3b23e 100%)}
.method-shade{position:absolute;inset:0;background:linear-gradient(90deg,rgba(0,0,0,.15),rgba(0,0,0,.55) 55%,rgba(0,0,0,.6))}
.method-mark{position:absolute;left:80px;top:142px;width:150px;height:150px;border:6px solid var(--green);border-radius:50%}
.method-rule{position:absolute;left:306px;top:126px;width:2px;height:200px;background:var(--white)}
.method-name{position:absolute;left:344px;top:170px;font-size:40px;font-weight:300;line-height:46px;color:var(--white);text-transform:uppercase}
.method-title{position:absolute;left:681px;top:72px;font-size:52px;font-weight:700;line-height:56px;color:var(--green);text-transform:uppercase;white-space:nowrap}
.method-text{position:absolute;left:681px;top:194px;width:470px;font-size:16px;line-height:26px;color:var(--white)}
.btn{position:absolute;height:50px;border:2px solid var(--white);border-radius:25px;font-size:16px;font-weight:500;text-transform:uppercase;display:flex;align-items:center;justify-content:center}
.method .btn{left:681px;top:324px;width:236px;color:var(--white)}

/* heritage */
.heritage{top:2262px;height:450px}
.heritage h2{position:absolute;top:72px;width:100%;text-align:center;font-size:29px;font-weight:700;text-transform:uppercase}
.heritage h2::after{content:"";display:block;width:200px;height:3px;background:var(--green);margin:6px auto 0}
.heritage p{position:absolute;top:150px;width:260px;text-align:center;font-size:14px;line-height:22px;font-weight:500;color:var(--ink)}
.heritage .btn{left:480px;top:320px;width:238px;border-color:var(--green);color:var(--green)}

/* numbers */
.numbers{top:2712px;height:444px;background:linear-gradient(180deg,#2c2e33,#4b4e55 40%,#5e5a4d 75%,#7a745c);color:var(--white);text-align:center}
.numbers h2{position:absolute;top:60px;width:100%;font-size:32px;font-weight:500;text-transform:uppercase}
.numbers h2 em{font-style:normal;color:var(--green)}
.numbers h2::after{content:"";display:block;width:150px;height:3px;background:var(--green);margin:6px auto 0}
.numbers .btn{left:480px;top:148px;width:240px;color:var(--white)}
.stat{position:absolute;top:262px;width:260px}
.stat b{display:block;font-size:90px;font-weight:700;color:var(--green);line-height:100px}
.stat span{display:block;font-size:14px;font-weight:500;text-transform:uppercase;margin-top:4px}

/* contact */
.contact{top:3156px;height:622px}
.contact h2{position:absolute;left:103px;top:50px;font-size:54px;font-weight:700;color:var(--green);text-transform:uppercase}
.contact .sub{position:absolute;left:103px;top:116px;font-size:20px;font-weight:700}
.addr-head{position:absolute;left:103px;top:176px;font-size:17px;font-weight:700;text-transform:uppercase;display:flex;align-items:center;gap:8px}
.addr{position:absolute;left:103px;top:208px;width:290px;font-size:14px;line-height:24px;color:var(--grey)}
.addr b{color:var(--ink)}
.social{position:absolute;left:103px;top:406px;display:flex;gap:14px;font-size:14px;font-weight:700;color:var(--green)}
.field{position:absolute;background:var(--green-soft);color:var(--white);font-size:13px;padding:12px 14px}
.send{position:absolute;left:470px;top:493px;width:142px;height:42px;background:var(--dark);color:var(--white);font-size:17px;font-weight:700;text-transform:uppercase;display:flex;align-items:center;justify-content:center}

/* footer */
.site-footer{top:3778px;height:76px}
.copy{position:absolute;left:118px;top:30px;font-size:13px;color:var(--dark)}
.copy b{font-weight:700}
.to-top{position:absolute;left:951px;top:28px;font-size:13px;color:var(--green);text-transform:uppercase;display:flex;align-items:center;gap:10px}
</style>
</head>
<body>

<header class="site-header">
  <div class="brand">TARVEK</div>
  <div class="brand-sub">Novelty Yarn Solutions</div>
  <nav class="main-nav">
    <span>Home</span><span>About us</span><span>Fluid</span><span>Partner method</span><span class="more">More</span>
  </nav>
</header>

<section class="hero" role="img" aria-label="Close-up photograph of colourful woven yarn samples in rows">
  <div class="hero-bar one">TAILORED</div>
  <div class="hero-bar two">WEAVING</div>
  <div class="hero-bar three">SOLUTIONS</div>
</section>
<div class="badge" style="top:888px" aria-label="40th anniversary badge"></div>

<section class="values">
  <div class="value" style="left:122px">
    <h3>Experience</h3>
    <p>Over the years the company has gained the knowledge and skills that define the superiority of our product and the rigor of our work ethic</p>
  </div>
  <div class="value" style="left:475px">
    <h3>Creativity</h3>
    <p>Our belief is that the key to our clients' success is a combination of innovation, creativity and quality. We strive to adapt and re-imagine our product, implementing these principles in order to meet and exceed our clients' demands (every time)</p>
  </div>
  <div class="value" style="left:813px">
    <h3>Professionality</h3>
    <p>We are a family business at the core. Our company is run with the same values as the Ferrani family: respect, determination and commitment.</p>
  </div>
</section>

<section class="offer-band">What we offer</section>
<section class="offer-tiles">
  <div class="tile network" role="img" aria-label="Photograph of dark woven fabric">
    <svg width="80" height="80" viewBox="0 0 80 80" fill="none" stroke="#fff" stroke-width="3">
      <circle cx="40" cy="40" r="11"/>
      <circle cx="40" cy="8" r="6"/><circle cx="40" cy="72" r="6"/>
      <circle cx="8" cy="40" r="6"/><circle cx="72" cy="40" r="6"/>
      <circle cx="17" cy="17" r="6"/><circle cx="63" cy="17" r="6"/>
      <circle cx="17" cy="63" r="6"/><circle cx="63" cy="63" r="6"/>
      <path d="M40 29V14M40 51v15M29 40H14M51 40h15M32 32l-11-11M48 32l11-11M32 48l-11 11M48 48l11 11"/>
    </svg>
    <h4>Network</h4>
    <p>A network of weavers, yarn producers and representatives consolidated over 40 years of successful business operations</p>
  </div>
  <div class="tile fabric" role="img" aria-label="Photograph of green woven fabric swatches"></div>
  <div class="tile production" role="img" aria-label="Photograph of red and ochre woven fabric">
    <svg width="80" height="80" viewBox="0 0 80 80" fill="none" stroke="#fff" stroke-width="3">
      <rect x="6" y="30" width="34" height="36"/>
      <rect x="46" y="12" width="28" height="54"/>
      <rect x="52" y="20" width="16" height="12"/>
      <path d="M6 44h34M14 30V18h18v12M52 42h16M52 50h16M2 70h76"/>
    </svg>
    <h4>Production</h4>
    <p>Production line is dynamic and solid, allowing for freedom as well as precision in any project</p>
  </div>
</section>

<section class="method" role="img" aria-label="Photograph of colourful woven yarn samples">
  <div class="method-shade"></div>
  <div class="method-mark"></div>
  <div class="method-rule"></div>
  <div class="method-name">Fluid<br>Partner<br>Method</div>
  <h2 class="method-title">Production built<br>around you</h2>
  <p class="method-text">Versatility and flexibility both in development and production are key in delivering a custom solution capable of giving life to your products.</p>
  <div class="btn">Find out more</div>
</section>
<div class="badge" style="top:2238px" aria-label="40th anniversary badge"></div>

<section class="heritage">
  <h2>Our heritage</h2>
  <p style="left:116px">Our team has decades of experience in providing yarn solutions to weavers around the world, assisting them in the creation of outstanding textiles.</p>
  <p style="left:470px">Our clients can expect open lines of communication, clarity and professionality</p>
  <p style="left:820px">Our focus is our client.<br>The success of a client is our success.</p>
  <div class="btn">Read more</div>
</section>

<section class="numbers" role="img" aria-label="Dark close-up photograph of woven textile">
  <h2>TYS in numbers <em>2017</em></h2>
  <div class="btn">Find out more</div>
  <div class="stat" style="left:135px"><b>40</b><span>Years in business</span></div>
  <div class="stat" style="left:487px"><b>2</b><span>Million kilograms/ yr</span></div>
  <div class="stat" style="left:841px"><b>8</b><span>Brands</span></div>
</section>

<section class="contact">
  <h2>Contact us</h2>
  <div class="sub">Tarvek Novelty Yarn Solutions</div>
  <div class="addr-head">
    <svg width="16" height="22" viewBox="0 0 16 22"><path d="M8 0a8 8 0 0 0-8 8c0 6 8 14 8 14s8-8 8-14a8 8 0 0 0-8-8z" fill="#1d1d1b"/><circle cx="8" cy="8" r="3" fill="#fff"/></svg>
    Address
  </div>
  <div class="addr">
    <b>Varnel s.r.l</b><br>
    Via dei Telai 41 - 50100 Fiorena - Italy - Tel. 0555 20418 r.a. - Fax 0555 207731<br>
    R.E.A FI 481902- Reg. Imp. FI 04718230592<br>
    <b>P.IVA 00528410633</b> - Cod. Fisc. 04718230592<br>
    Capitale sociale € 84.300,00 int. ver.
  </div>
  <div class="social"><span>Chirp</span><span>Pagebook</span><span>Linkwork</span><span>Vidtube</span></div>

  <div class="field" style="left:470px;top:172px;width:260px;height:42px">Name</div>
  <div class="field" style="left:753px;top:172px;width:260px;height:42px">Email</div>
  <div class="field" style="left:470px;top:236px;width:260px;height:42px">Website</div>
  <div class="field" style="left:753px;top:236px;width:260px;height:42px">Subject</div>
  <div class="field" style="left:470px;top:295px;width:543px;height:173px">Message</div>
  <div class="send">Send</div>
</section>

<footer class="site-footer">
  <div class="copy">© 2018 <b>TARVEK NOVELTY YARN SOLUTIONS</b>. All Rights Reserved.</div>
  <div class="to-top">Back to top
    <svg width="26" height="16" viewBox="0 0 26 16"><path d="M1 15L13 2l12 13" fill="none" stroke="#1d1d1b" stroke-width="2"/></svg>
  </div>
</footer>

</body>
</html>
```